Real Estate "For Sale" Sign for construction company

We need a sign that we can use to hang on a post and place on the road when we sell a property. The sign will be simple and will need to mainly feature our logo (files attached), as well as the words "For Sale", and then our phone number "(555) 617 3489". The sign will hang on a post that'll look something like the attached picture.

Target Market(s)

Home buyers

Industry/Entity Type

Real Estate

Font styles to use
Serif
Sans Serif

Colors
0054AA
0677BA
7BADD7
CADEEF
E8F1F8
0094D4
00A9DD
6FCCEA
C7EBF8
E9F6FB

Requirements
Must have
• For Sale & our phone number

```html
<!DOCTYPE html>
<html lang="en">
<head>
<meta charset="utf-8">
<title>Highland Crest Homes – For Sale Sign</title>
<link href="https://fonts.googleapis.com/css2?family=Montserrat:wght@400;800&display=swap" rel="stylesheet">
<style>
  :root {
    --page-bg: #ffffff;
    --sign-bg: #f8f8fd;
    --brand-blue: #1b86c8;
    --sky-blue: #0fa0dc;
    --navy: #233a7a;
    --mark-blue: #0677ba;
    --band-light: #9fdcf3;
    --band-deep: #3a78ba;
  }
  html, body {
    margin: 0;
    width: 1200px;
    height: 1200px;
    overflow: hidden;
    background: var(--page-bg);
  }
  .sign {
    position: absolute;
    left: 82px;
    top: 0;
    width: 1036px;
    height: 1200px;
    background: var(--sign-bg);
    overflow: hidden;
    font-family: "Montserrat", sans-serif;
  }
  .brand-mark {
    position: absolute;
    left: 368px;
    top: 70px;
    width: 300px;
    height: 300px;
    border-radius: 50%;
    background: var(--mark-blue);
  }
  .brand-name {
    position: absolute;
    left: 0;
    right: 0;
    top: 410px;
    text-align: center;
    color: var(--brand-blue);
    font-weight: 400;
    line-height: 1;
  }
  .brand-name .name-main {
    display: block;
    font-size: 86px;
    letter-spacing: -1px;
  }
  .brand-name .name-sub {
    display: block;
    margin-top: 22px;
    font-size: 24px;
    letter-spacing: 0.9em;
    padding-left: 0.9em;
  }
  .headline {
    position: absolute;
    left: 0;
    right: 0;
    top: 618px;
    margin: 0;
    text-align: center;
    font-size: 172px;
    font-weight: 800;
    letter-spacing: -3px;
    line-height: 1;
  }
  .headline .word-for { color: var(--sky-blue); }
  .headline .word-sale { color: var(--navy); }
  .phone {
    position: absolute;
    left: 0;
    right: 0;
    top: 834px;
    text-align: center;
    font-size: 84px;
    font-weight: 800;
    letter-spacing: 0.16em;
    padding-left: 0.16em;
    color: var(--navy);
    line-height: 1;
  }
  .mountain-scene {
    position: absolute;
    left: 0;
    right: 0;
    bottom: 0;
    height: 235px;
    background: linear-gradient(to bottom, var(--band-light), var(--band-deep));
  }
</style>
</head>
<body>
  <div class="sign">
    <div class="brand-mark" aria-hidden="true"></div>
    <div class="brand-name">
      <span class="name-main">Highland Crest</span>
      <span class="name-sub">HOMES</span>
    </div>
    <h1 class="headline"><span class="word-for">FOR</span><span class="word-sale">SALE</span></h1>
    <div class="phone">(555) 617 3489</div>
    <div class="mountain-scene" role="img" aria-label="Illustration of layered blue mountain ridges along the bottom of the sign"></div>
  </div>
</body>
</html>
```